Redesign of Form/Document Navigation Page

I need a redesign of our document and navigation bar on the left. We want the same navigation bar layout/setup but want the buttons and typography to be simple and matching all over. The form needs to be aesthetically pleasing and fit within the page.

1st attachment is our Direct Deposit and the second is the form continued.

```html
<!DOCTYPE html>
<html lang="en">
<head>
<meta charset="utf-8">
<title>Sentinel Watch Services – Direct Deposit</title>
<link href="https://fonts.googleapis.com/css2?family=Roboto:wght@300;400;500;700&display=swap" rel="stylesheet">
<style>
:root{
  --blue:#12548f;
  --blue-edge:#0d3c6b;
  --gold:#f0b71b;
  --ink:#222;
  --text:#444;
  --muted:#999;
  --line:#cfcfcf;
  --panel-line:#d6d6d6;
  --scroll-track:#f1f1f1;
  --scroll-thumb:#c1c1c1;
  --nav-blue:#1b4f86;
}
*{box-sizing:border-box;margin:0;padding:0}
html,body{width:1200px;height:849px;overflow:hidden;background:#fff;font-family:'Roboto',sans-serif;color:var(--text)}
.page{position:relative;width:1200px;height:849px}

.brand{position:absolute;left:99px;top:22px;display:flex;align-items:center;gap:8px}
.brand-dot{width:38px;height:38px;border-radius:50%;background:var(--blue)}
.brand-name{color:var(--gold);font-weight:700;font-size:21px;line-height:21px;width:190px;text-transform:uppercase}

.topnav{position:absolute;top:23px;left:600px;display:flex;align-items:center;height:38px}
.topnav a{text-decoration:none;font-weight:500;font-size:14px;color:var(--ink);display:flex;align-items:center;gap:6px;position:absolute;white-space:nowrap}
.topnav .home{left:24px}
.topnav .help{left:130px}
.topnav .user{left:227px;color:var(--nav-blue)}
.topnav .back{left:366px;top:0;width:135px;height:38px;background:var(--gold);color:#fff;justify-content:center;font-weight:400;font-size:13.5px}

.sidebar{position:absolute;left:99px;top:93px;width:276px;height:679px;background:var(--blue);border:2px solid var(--blue-edge)}
.sidebar a{display:flex;align-items:center;height:97px;border-bottom:2px solid var(--blue-edge);color:#fff;text-decoration:none;font-weight:500;font-size:15.5px;text-transform:uppercase}
.sidebar a:last-child{border-bottom:none}
.sidebar svg{width:38px;height:38px;margin-left:17px;margin-right:16px;flex:none}

.panel{position:absolute;left:405px;top:93px;width:695px;height:683px;border:1px solid var(--panel-line)}
.scrollbar{position:absolute;right:0;top:0;width:15px;height:100%;background:var(--scroll-track)}
.scrollbar span{position:absolute;left:0;top:256px;width:15px;height:99px;background:var(--scroll-thumb)}

.doc-title{position:absolute;left:23px;top:24px;font-size:14.5px;color:var(--ink);font-weight:400}
.doc-title strong{font-size:17px;font-weight:500}
.doc-body{position:absolute;left:22px;top:50px;width:640px;font-size:10.7px;font-weight:300;line-height:20.6px;color:var(--text)}
.doc-body p{margin-bottom:8px}
.doc-body .note{margin-top:24px}

.field{position:absolute;height:32px;border:1px solid var(--line);font-size:10.7px;font-style:italic;font-weight:300;color:var(--muted);padding:10px 11px}
.btn{position:absolute;background:var(--gold);color:#fff;font-weight:500;text-transform:uppercase;display:flex;align-items:center;justify-content:center}
.btn-accept{left:22px;top:345px;width:154px;height:36px;font-size:14.5px}

.payroll{position:absolute;left:23px;top:428px;width:637px;height:226px;border:1px solid var(--line)}
.payroll h2{position:absolute;top:24px;width:100%;text-align:center;font-size:14.5px;font-weight:500;color:var(--ink)}
.btn-send{left:23px;top:182px;width:90px;height:30px;font-size:13px;font-weight:400}

.footer-line{position:absolute;left:99px;top:804px;width:1002px;border-top:1px solid var(--line)}
.footer{position:absolute;top:820px;left:99px;width:1002px;text-align:center;font-size:11px;color:var(--text)}
</style>
</head>
<body>
<div class="page">
  <div class="brand"><span class="brand-dot"></span><span class="brand-name">Sentinel Watch Services</span></div>

  <nav class="topnav">
    <a class="home" href="#">HOME
      <svg width="12" height="11" viewBox="0 0 12 11"><path d="M6 0 0 5.5h1.6V11h3.2V7.5h2.4V11h3.2V5.5H12z" fill="#222"/></svg></a>
    <a class="help" href="#">HELP <b style="font-weight:700">?</b></a>
    <a class="user" href="#">DANA MERCER
      <svg width="12" height="12" viewBox="0 0 12 12"><path d="M3.5 2.5a4.5 4.5 0 1 0 5 0" fill="none" stroke="#1b4f86" stroke-width="1.8"/><path d="M6 0v5.5" stroke="#1b4f86" stroke-width="1.8"/></svg></a>
    <a class="back" href="#">BACK TO PROFILE</a>
  </nav>

  <aside class="sidebar">
    <a href="#"><svg viewBox="0 0 38 38"><circle cx="22" cy="21" r="15" fill="#fff"/><text x="22" y="28" font-size="19" font-weight="700" text-anchor="middle" fill="#12548f" font-family="Roboto,sans-serif">$</text><path d="M4 2v9M1 8l3 4 3-4" stroke="#fff" stroke-width="2" fill="none"/></svg>Direct Deposit</a>
    <a href="#"><svg viewBox="0 0 38 38" fill="none" stroke="#fff" stroke-width="2.4"><rect x="2" y="3" width="34" height="26"/><path d="M8 11h22M8 17h12"/><circle cx="25" cy="28" r="5" fill="#fff"/></svg>Change W-4</a>
    <a href="#"><svg viewBox="0 0 38 38" stroke="#fff" stroke-width="4" fill="none"><path d="M6 34 28 10M32 34 12 12"/><path d="M5 10l8-6 6 5" stroke-width="3"/><circle cx="30" cy="8" r="5" stroke-width="3"/></svg>Labour Code</a>
    <a href="#"><svg viewBox="0 0 38 38"><circle cx="19" cy="19" r="17" fill="none" stroke="#fff" stroke-width="2.4"/><text x="19" y="28" font-size="24" font-style="italic" font-weight="700" text-anchor="middle" fill="#fff" font-family="serif">i</text></svg>Personal Information</a>
    <a href="#"><svg viewBox="0 0 38 38" fill="#fff"><rect x="2" y="16" width="6" height="19"/><path d="M11 16 20 4c3-1 4 1 3 4l-2 7h11c3 0 4 3 2 5l-2 12c-1 2-2 3-4 3H11z"/></svg>Appraisal &amp; Review</a>
    <a href="#"><svg viewBox="0 0 38 38" fill="none" stroke="#fff" stroke-width="2.4"><rect x="7" y="3" width="24" height="31"/><path d="M12 11h14M12 17h14M12 23h14M12 29h9"/></svg>Write Up-Slip</a>
    <a href="#"><svg viewBox="0 0 38 38" fill="#fff"><rect x="3" y="28" width="4" height="8"/><rect x="9" y="25" width="4" height="11"/><rect x="15" y="22" width="4" height="14"/><rect x="21" y="18" width="4" height="18"/><rect x="27" y="13" width="4" height="23"/><path d="M3 24 26 6" stroke="#fff" stroke-width="2.4"/><path d="M22 4h9v9z"/></svg>Employee Performance</a>
  </aside>

  <main class="panel">
    <h1 class="doc-title"><strong>IMPORTANT!</strong> PLEASE READ AND SIGN BEFORE COMPLETING AND SUBMITTING</h1>
    <div class="doc-body">
      <p>I hereby authorize SENTINEL WATCH SERVICES to deposit any amounts owed me, as instructed by my employer, by initiating credit entries to my account at the financial institution (hereinafter "Bank") indicated on this form. Further, I authorize Bank to accept and to credit any credit entries indicated by SENTINEL WATCH SERVICES to my account. In the event that SENTINEL WATCH SERVICES deposits funds erroneously into my account, I authorize SENTINEL WATCH SERVICES to debit my account for an amount not to exceed the original amount of the erroneous credit.</p>
      <p>This authorization is to remain in full force and effect until SENTINEL WATCH SERVICES and Bank have received written notice from me of its termination in such time and in such manner as to afford SENTINEL WATCH SERVICES and Bank reasonable opportunity to act on it.</p>
      <p class="note">The last item must be for the remaining amount owed to you. To distribute to more accounts, please complete another form.</p>
    </div>

    <div class="field" style="left:24px;top:295px;width:204px">Employee Name</div>
    <div class="field" style="left:240px;top:295px;width:204px">Employee Signature</div>
    <div class="field" style="left:457px;top:295px;width:203px">Sign Date</div>
    <div class="btn btn-accept">Accept Document</div>

    <section class="payroll">
      <h2>ONLY PAYROLL MANAGER SIGNS BELOW</h2>
      <div class="field" style="left:25px;top:58px;width:285px">Company Name</div>
      <div class="field" style="left:325px;top:58px;width:286px">Employee File Number</div>
      <div class="field" style="left:25px;top:101px;width:586px;height:69px">Comments</div>
      <div class="btn btn-send">Send Now</div>
    </section>

    <div class="scrollbar"><span></span></div>
  </main>

  <div class="footer-line"></div>
  <footer class="footer">© 2016 Company name, Inc. All rights reserved.</footer>
</div>
</body>
</html>
```